Business Plan Template

Hi, I work as a Business Growth Coach and I use this Business Plan template in my work. It looks a bit old-fashioned so I would like it updated to give it a professional up-to-date look. In particular, the 5 images need to be replaced/re-sized.

Marcus

Business

```html
<!DOCTYPE html>
<html lang="en">
<head>
<meta charset="utf-8">
<title>Business Plan – Vision to Actions</title>
<link rel="stylesheet" href="https://fonts.googleapis.com/css2?family=Tinos:wght@400;700&display=swap">
<style>
  :root {
    --ink: #1c1c1c;
    --paper: #ffffff;
    --vision-a: #ffffff;
    --vision-b: #f3b6d6;
    --mission-a: #fbf08a;
    --mission-b: #fbe3ef;
    --strategy-a: #ffffff;
    --strategy-b: #a9e2c3;
    --objective-a: #78d3e0;
    --objective-b: #eef6f4;
    --action-a: #cdeee0;
    --action-b: #fbd0b2;
    --band-h: 232px;
    --gap: 10px;
    --photo-w: 375px;
  }
  * { box-sizing: border-box; margin: 0; padding: 0; }
  html, body { width: 851px; height: 1200px; overflow: hidden; background: var(--paper); }
  .plan {
    width: 851px; height: 1200px;
    display: flex; flex-direction: column; gap: var(--gap);
  }
  .stage {
    position: relative; height: var(--band-h); flex: none;
  }
  .stage--vision    { background: linear-gradient(90deg, var(--vision-a) 10%, var(--vision-b)); }
  .stage--mission   { background: linear-gradient(90deg, var(--mission-a), var(--mission-b) 90%); }
  .stage--strategy  { background: linear-gradient(90deg, var(--strategy-a) 10%, var(--strategy-b)); }
  .stage--objective { background: linear-gradient(90deg, var(--objective-a), var(--objective-b) 90%); }
  .stage--action    { background: linear-gradient(90deg, var(--action-a), var(--action-b)); }

  .stage__label {
    position: absolute; top: 0; height: 100%;
    display: flex; align-items: center; justify-content: center;
    width: 44px;
    font-family: "Tinos", "Times New Roman", serif;
    font-weight: 400;
    font-size: 27px; letter-spacing: 3px; color: var(--ink);
    writing-mode: vertical-rl;
  }
  .stage__label--left  { left: 4px; transform: rotate(180deg); }
  .stage__label--right { right: 4px; }

  .stage__photo {
    position: absolute; top: 0; height: 100%; width: var(--photo-w);
  }
  .stage__photo--left  { left: 50px;  border-radius: 0 116px 116px 0; }
  .stage__photo--right { right: 98px; border-radius: 116px 0 0 116px; }

  .photo--eye {
    background: linear-gradient(90deg, #b9b6b3, #8f9f94 45%, #6f8fa6 70%, #c7c3c0);
  }
  .photo--rocket {
    background: linear-gradient(180deg, #5f8fc2 0%, #9ab8d8 45%, #e7c6a0 75%, #d9862f 100%);
  }
  .photo--chess {
    background: linear-gradient(90deg, #3a3a3a, #8d8d8d 45%, #dcdcdc);
  }
  .photo--target {
    background: linear-gradient(90deg, #c9a3a3, #d9d6d6 45%, #c9d3d9 75%, #b6d6e6);
  }
  .photo--watch {
    background: linear-gradient(135deg, #e9f3e4, #9fc0d8 55%, #3b5f8f);
  }
</style>
</head>
<body>
<main class="plan">
  <section class="stage stage--vision">
    <h2 class="stage__label stage__label--left">VISION</h2>
    <div class="stage__photo stage__photo--left photo--eye" role="img" aria-label="Close-up photograph of a human eye with a multicoloured iris"></div>
  </section>

  <section class="stage stage--mission">
    <div class="stage__photo stage__photo--right photo--rocket" role="img" aria-label="Photograph of a rocket launching into a blue sky"></div>
    <h2 class="stage__label stage__label--right">MISSION</h2>
  </section>

  <section class="stage stage--strategy">
    <h2 class="stage__label stage__label--left">STRATEGIES</h2>
    <div class="stage__photo stage__photo--left photo--chess" role="img" aria-label="Black-and-white photograph of chess pieces on a board"></div>
  </section>

  <section class="stage stage--objective">
    <div class="stage__photo stage__photo--right photo--target" role="img" aria-label="Illustration of an arrow hitting the centre of a red target"></div>
    <h2 class="stage__label stage__label--right">OBJECTIVES</h2>
  </section>

  <section class="stage stage--action">
    <h2 class="stage__label stage__label--left">ACTIONS</h2>
    <div class="stage__photo stage__photo--left photo--watch" role="img" aria-label="Illustration of a blue stopwatch over a world map"></div>
  </section>
</main>
</body>
</html>
```